Girls & Tween Birthday Hotspot

Looking to refresh our old business cards. We are a girls/tween birthday party store and salon specializing in princess, glamour and spa parties. I would like to maintain the same colors (hot pink and turquoise). Would like the card to be feminine, fun and glitzy..

Target Market(s)

Parents of girls and girls aged 4-14

Industry/Entity Type

Store

Font styles to use
Script

Colors
e34197
85cae6

Requirements
Must have
• name phone and address
colors of hot pink and turquoise
appointment day and time field on one side
Nice to have
• creativity
Should not have
• picture of lipstick

```html
<!DOCTYPE html>
<html lang="en">
<head>
<meta charset="utf-8">
<title>Twirl Party Studio – Business Card</title>
<link rel="stylesheet" href="https://fonts.googleapis.com/css2?family=Dancing+Script:wght@600;700&display=swap">
<style>
  :root {
    --hot-pink: #e34197;
    --turquoise: #85cae6;
    --blush: #f7b8d8;
    --blush-deep: #f3a3cb;
    --white: #ffffff;
    --backdrop: #3e3330;
  }
  * { box-sizing: border-box; margin: 0; padding: 0; }
  html, body { width: 1200px; height: 539px; overflow: hidden; }
  body {
    background: var(--backdrop);
    font-family: "Dancing Script", cursive;
    color: var(--white);
    position: relative;
  }

  .card {
    position: absolute;
    top: 115px;
    width: 540px;
    height: 309px;
    border-radius: 16px;
    overflow: hidden;
    box-shadow: 0 8px 22px rgba(0,0,0,.35);
  }

  /* ---------- Appointment side ---------- */
  .card--appointment { left: 30px; display: flex; }
  .contact-column {
    width: 170px;
    background: var(--hot-pink);
    padding: 28px 18px;
    display: flex;
    flex-direction: column;
    align-items: center;
  }
  .contact-name {
    align-self: flex-start;
    font-size: 26px;
    font-weight: 700;
    margin-bottom: 22px;
  }
  .contact-icon {
    width: 46px; height: 34px;
    background: var(--white);
    border-radius: 8px;
    display: flex; align-items: center; justify-content: center;
    margin-bottom: 6px;
  }
  .contact-phone {
    font-size: 19px; font-weight: 700;
    letter-spacing: 1px;
    margin-bottom: 16px;
  }
  .contact-address {
    align-self: flex-start;
    font-size: 17px; font-weight: 700;
    line-height: 1.15;
    margin-top: 4px;
  }

  .appointment-panel {
    flex: 1;
    background: var(--turquoise);
    padding: 20px 34px 0 40px;
  }
  .silhouette {
    display: block;
    width: 46px; height: 52px;
    margin: 0 auto;
    background: var(--hot-pink);
    border-radius: 50% 50% 40% 40%;
  }
  .title-rule {
    display: block;
    height: 3px; width: 220px;
    margin: 8px auto 8px;
    background: linear-gradient(90deg, transparent, var(--hot-pink), transparent);
    border-radius: 2px;
  }
  .appointment-title {
    display: block;
    width: max-content;
    margin: 0 auto 30px;
    background: var(--hot-pink);
    padding: 2px 16px 4px;
    font-size: 24px;
    font-weight: 700;
  }
  .appointment-field {
    display: flex; align-items: baseline;
    font-size: 24px; font-weight: 700;
    margin-bottom: 10px;
  }
  .appointment-field .blank {
    flex: 1;
    margin-left: 10px;
    border-bottom: 2px dotted var(--white);
  }
  .appointment-tagline {
    text-align: right;
    font-size: 15px; font-weight: 600;
    margin-top: 10px;
  }

  /* ---------- Brand side ---------- */
  .card--brand {
    left: 630px;
    background: linear-gradient(160deg, var(--blush) 0%, var(--blush-deep) 100%);
    display: flex; flex-direction: column;
    align-items: center; justify-content: center;
  }
  .brand-name {
    font-size: 40px;
    font-weight: 700;
    color: var(--hot-pink);
  }
  .brand-services {
    margin-top: 14px;
    font-size: 24px; font-weight: 700;
    color: var(--hot-pink);
    letter-spacing: 1px;
  }
</style>
</head>
<body>

  <section class="card card--appointment">
    <aside class="contact-column">
      <p class="contact-name">Rosalie</p>

      <span class="contact-icon">
        <svg width="22" height="22" viewBox="0 0 24 24" aria-hidden="true">
          <path fill="#85cae6" d="M6.6 10.8a15.1 15.1 0 0 0 6.6 6.6l2.2-2.2a1 1 0 0 1 1-.25 11.4 11.4 0 0 0 3.6.57 1 1 0 0 1 1 1V20a1 1 0 0 1-1 1A17 17 0 0 1 3 4a1 1 0 0 1 1-1h3.5a1 1 0 0 1 1 1c0 1.25.2 2.45.57 3.6a1 1 0 0 1-.25 1z"/>
        </svg>
      </span>
      <p class="contact-phone">555.210.4837</p>

      <span class="contact-icon">
        <svg width="20" height="24" viewBox="0 0 24 24" aria-hidden="true">
          <path fill="#85cae6" d="M12 2a7 7 0 0 0-7 7c0 5.2 7 13 7 13s7-7.8 7-13a7 7 0 0 0-7-7zm0 9.5A2.5 2.5 0 1 1 12 6.5a2.5 2.5 0 0 1 0 5z"/>
        </svg>
      </span>
      <p class="contact-address">48 Maple Grove<br>lane Brookfield<br>Ohio 44021.</p>
    </aside>

    <div class="appointment-panel">
      <span class="silhouette" role="img" aria-label="Pink silhouette of a girl with a ponytail"></span>
      <span class="title-rule"></span>
      <h2 class="appointment-title">Next Appointment</h2>
      <p class="appointment-field">Date <span class="blank"></span></p>
      <p class="appointment-field">Time <span class="blank"></span></p>
      <p class="appointment-tagline">We know what girls want</p>
    </div>
  </section>

  <section class="card card--brand">
    <p class="brand-name">Twirl Party Studio</p>
    <p class="brand-services">Spa • Parties • Boutique</p>
  </section>

</body>
</html>
```